Thornbury Lettings Managment Ltd website

Need a website To inform people/clients of the services we provide. 5 pages total with a local feel. Bristol, UK. I have logo artwork already is like the look based on
incorporate the artwork attached for theme, feel and colours fonts info etc

To best describe the business have a brief look at www.fernwickhomes.example.co.uk which is a local firm offering the same services. This is for your ref only and not to be copied.

Target Market(s)

Property Investors/Landlords

Coding

Coded - Design and coding required

Number of Pages Required

5+ page

Colors
0392cd
f68d4d

Requirements
Must have
• local feel. Possibly using some local architecture or historic landmarks etc. This is fexible.
• most also be mobile device compatible
Nice to have
• the membership logos - files attached: YQK, JZV, QXW and safehold-example.co.uk

```html
<!DOCTYPE html>
<html lang="en">
<head>
<meta charset="utf-8">
<title>Thornbury Lettings Managment Ltd</title>
<link href="https://fonts.googleapis.com/css2?family=Open+Sans:wght@400;600;700&family=Roboto+Condensed:wght@400;700&display=swap" rel="stylesheet">
<style>
:root{
  --blue:#0392cd;
  --blue-deep:#0a7fbd;
  --orange:#f68d4d;
  --navy:#1d4a63;
  --ink:#2b2b2b;
  --body:#6b6b6b;
  --muted:#f1f3f5;
  --band:#e9edf1;
  --footer-dark:#111417;
  --white:#ffffff;
}
*{box-sizing:border-box;margin:0;padding:0}
html,body{width:1200px;height:2655px;overflow:hidden;background:var(--white)}
body{font-family:"Open Sans",Arial,sans-serif;color:var(--body);font-size:12px;line-height:1.75}
a{text-decoration:none;color:inherit}
.wrap{width:1036px;margin:0 auto;position:relative}

/* header */
.site-header{height:115px;display:flex;align-items:center;justify-content:space-between;padding:0 88px;background:var(--white)}
.brand{display:flex;align-items:center;gap:10px;color:var(--navy);font-weight:700}
.brand-mark{width:44px;height:44px;background:var(--blue)}
.brand-name{font-size:25px;line-height:1}
.brand-sub{font-size:11px;line-height:1.2;display:block;margin-top:3px}
.main-nav{display:flex;align-items:center;gap:34px;font-size:12px;font-weight:600;color:#333;text-transform:uppercase}
.main-nav .current{color:var(--blue)}
.search-btn{width:36px;height:36px;border:1px solid #ddd;display:flex;align-items:center;justify-content:center}

/* hero */
.hero{height:597px;position:relative;background:linear-gradient(180deg,#6f7f8c 0%,#a89668 35%,#b68a45 60%,#5f5236 100%)}
.hero-caption{position:absolute;left:580px;top:326px;width:532px;height:132px;background:rgba(26,70,90,.82);color:var(--white);font-family:"Roboto Condensed",Arial,sans-serif;text-align:center;padding-top:24px;white-space:nowrap}
.hero-caption h1{font-size:30px;font-weight:400;line-height:1.25;text-transform:uppercase}
.hero-caption p{font-size:25px;line-height:1.4;margin-top:2px}
.slider-arrows{position:absolute;left:1028px;top:487px;display:flex;gap:6px}
.slider-arrows span{width:34px;height:34px;background:rgba(0,0,0,.55);display:flex;align-items:center;justify-content:center}

/* section headings */
.section-title{font-size:20px;font-weight:600;color:var(--ink);text-transform:uppercase;text-align:center;letter-spacing:.2px}
.section-title em{font-style:normal;color:var(--orange)}

.welcome{height:228px;padding-top:45px;text-align:center}
.welcome p{margin-top:14px;font-size:11.5px;line-height:1.95;padding:0 4px}

/* services */
.services{height:530px;background:var(--band);padding-top:38px}
.services .lead{text-align:center;font-size:14px;font-weight:600;color:#444;margin-top:10px}
.service-grid{display:flex;gap:22px;margin-top:28px}
.service{width:331px}
.service-photo{height:200px;border:7px solid var(--white);box-shadow:0 1px 4px rgba(0,0,0,.15)}
.photo-keys{background:linear-gradient(135deg,#c9b39e,#e8ddd4 60%,#f1ebe6)}
.photo-couple{background:linear-gradient(135deg,#e7c39a,#f3e3cf 55%,#a9c1d4)}
.photo-handshake{background:linear-gradient(135deg,#d9d9d9,#c8302f 45%,#4a5668)}
.service h3{margin-top:22px;font-size:15px;font-weight:600;color:var(--blue);text-transform:uppercase}
.service p{font-size:11px;line-height:1.8;margin-top:6px}
.read-link{display:block;margin-top:10px;font-size:10.5px;color:var(--orange)}

/* about */
.about{height:435px;padding-top:78px}
.about .wrap{display:flex;gap:36px}
.video{width:484px;height:297px;border:7px solid var(--white);box-shadow:0 1px 6px rgba(0,0,0,.25);position:relative;background:#222}
.video-frame{position:absolute;inset:0 0 36px 0;background:linear-gradient(180deg,#3f6ea1 0%,#8aa7c4 35%,#9b8263 60%,#5a4a3a 100%)}
.play{position:absolute;left:50%;top:45%;transform:translate(-50%,-50%)}
.video-bar{position:absolute;left:0;right:0;bottom:0;height:36px;background:#161616;display:flex;align-items:center;gap:10px;padding:0 12px;color:#ccc;font-size:10px}
.video-track{flex:1;height:3px;background:#555;position:relative}
.video-track i{position:absolute;left:0;top:0;height:3px;width:18%;background:#c0392b}
.about-copy{flex:1}
.about-copy .section-title{text-align:left;font-size:19px}
.about-copy p{font-size:11.5px;line-height:1.95;margin-top:16px}
.btn{display:inline-block;margin-top:26px;background:var(--blue);color:var(--white);font-size:13px;font-weight:600;padding:9px 30px;border-radius:2px}

/* testimonials */
.testimonials{height:275px;background:var(--muted);padding-top:38px}
.testimonials .section-title{color:var(--orange)}
.quotes{display:flex;justify-content:space-between;margin-top:28px}
.quote{width:470px;display:flex;gap:24px;padding-left:20px}
.avatar{width:80px;height:80px;border-radius:50%;flex:none;border:3px solid var(--white)}
.avatar-a{background:linear-gradient(180deg,#d9c1a8,#6c8aa8)}
.avatar-b{background:linear-gradient(180deg,#8a6a4e,#e6d3c0)}
.quote-body{position:relative;padding-left:18px;width:320px}
.quote-body::before,.quote-body::after{position:absolute;font-family:Georgia,serif;font-size:42px;color:#bbb;line-height:1}
.quote-body::before{content:"\201C";left:-6px;top:-12px}
.quote-body::after{content:"\201D";right:-14px;top:42px}
.quote-body p{font-size:11px;line-height:1.85;color:#555}
.quote-body strong{display:block;margin-top:6px;font-size:10.5px;color:var(--blue);text-transform:uppercase}
.quote-body span{font-size:11px;color:#555}

/* memberships */
.memberships{height:170px;display:flex;align-items:center}
.memberships .wrap{display:flex;align-items:center;justify-content:space-between}
.memberships h4{font-size:20px;font-weight:600;line-height:1.35;color:var(--blue);text-transform:uppercase}
.memberships h4 em{font-style:normal;color:var(--orange)}
.member{display:flex;align-items:center;gap:10px;font-size:20px;font-weight:700;color:#3a3a3a}
.member-badge{width:48px;height:48px}

/* footer */
.site-footer{height:235px;background:var(--blue-deep);color:var(--white);padding-top:42px}
.footer-cols{display:flex}
.footer-col{font-size:11px;line-height:1.7}
.footer-col h5{font-size:15px;font-weight:600;text-transform:uppercase;margin-bottom:10px}
.col-news{width:297px}
.col-tweet{width:298px}
.col-contact{width:278px}
.col-follow{flex:1}
.email-field{margin-top:12px;width:216px;height:30px;background:var(--white);color:#888;font-size:10.5px;padding:6px 10px}
.subscribe{margin-top:10px;display:inline-block;background:var(--orange);color:var(--white);font-size:10px;font-weight:600;padding:5px 14px;border-radius:2px}
.tweet{display:flex;gap:10px;margin-bottom:12px}
.tweet-dot{width:14px;height:14px;border-radius:50%;background:var(--white);flex:none;margin-top:3px}
.tweet em{opacity:.85}
.contact-list li{list-style:none;margin-bottom:14px}
.social li{list-style:none;display:flex;align-items:center;gap:14px;margin-bottom:10px}
.social-dot{width:33px;height:33px;border-radius:50%;border:1px solid rgba(255,255,255,.7)}
.copyright{height:70px;background:var(--footer-dark);color:#ddd;font-size:11px;display:flex;align-items:center;justify-content:center}
</style>
</head>
<body>

<header class="site-header">
  <a class="brand" href="#">
    <span class="brand-mark"></span>
    <span><span class="brand-name">Thornbury</span><span class="brand-sub">lettings managment ltd</span></span>
  </a>
  <nav class="main-nav">
    <a class="current" href="#">Home</a>
    <a href="#">About Us</a>
    <a href="#">Services</a>
    <a href="#">Projects</a>
    <a href="#">Testimonials</a>
    <a href="#">Contact Us</a>
    <span class="search-btn"><svg width="12" height="12" viewBox="0 0 12 12"><circle cx="5" cy="5" r="3.6" fill="none" stroke="#777" stroke-width="1.4"/><line x1="7.6" y1="7.6" x2="11" y2="11" stroke="#777" stroke-width="1.4"/></svg></span>
  </nav>
</header>

<section class="hero" role="img" aria-label="Historic Bristol gothic stone building under a cloudy sky">
  <div class="hero-caption">
    <h1>Thornbury Lettings Managment Ltd</h1>
    <p>Neque porro quisquam est qui dolorem ipsum</p>
  </div>
  <div class="slider-arrows">
    <span><svg width="10" height="14" viewBox="0 0 10 14"><path d="M7 2 2 7l5 5" fill="none" stroke="#fff" stroke-width="2"/></svg></span>
    <span><svg width="10" height="14" viewBox="0 0 10 14"><path d="M3 2l5 5-5 5" fill="none" stroke="#fff" stroke-width="2"/></svg></span>
  </div>
</section>

<section class="welcome">
  <div class="wrap">
    <h2 class="section-title">Welcome to <em>Thornbury Lettings Managment Ltd</em></h2>
    <p>Lorem Ipsum has been the industry's standard dummy text ever since the 1500s, when an unknown printer took a galley of type and scrambled it to make a type specimen book. It has survived not only five centuries, but also the leap into electronic typesetting, remaining essentially unchanged. It was popularised in the 1960s with the release of Dryletter sheets containing Lorem Ipsum passages, and more recently with desktop publishing software like Pagecraft Studio including versions of Lorem Ipsum.</p>
  </div>
</section>

<section class="services">
  <div class="wrap">
    <h2 class="section-title">We Provide <em>Services</em></h2>
    <p class="lead">Lorem Ipsum is simply dummy text of the printing and typesetting industry</p>
    <div class="service-grid">
      <article class="service">
        <div class="service-photo photo-keys" role="img" aria-label="Hand holding house keys"></div>
        <h3>For Landlords</h3>
        <p>Lorem Ipsum has been the industry's standard dummy text ever since the 1500s, when an unknown printer took a galley of type and scrambled it to make a type specimen book.</p>
        <a class="read-link" href="#">Read More »</a>
      </article>
      <article class="service">
        <div class="service-photo photo-couple" role="img" aria-label="Tenant couple holding a small model house"></div>
        <h3>For Tenants</h3>
        <p>Lorem Ipsum has been the industry's standard dummy text ever since the 1500s, when an unknown printer took a galley of type and scrambled it to make a type specimen book.</p>
        <a class="read-link" href="#">Read More »</a>
      </article>
      <article class="service">
        <div class="service-photo photo-handshake" role="img" aria-label="Agents shaking hands over a model house"></div>
        <h3>For Agencies</h3>
        <p>Lorem Ipsum has been the industry's standard dummy text ever since the 1500s, when an unknown printer took a galley of type and scrambled it to make a type specimen book.</p>
        <a class="read-link" href="#">Read More »</a>
      </article>
    </div>
  </div>
</section>

<section class="about">
  <div class="wrap">
    <div class="video">
      <div class="video-frame" role="img" aria-label="Video still of the Bristol city skyline"></div>
      <svg class="play" width="50" height="50" viewBox="0 0 50 50"><circle cx="25" cy="25" r="24" fill="rgba(0,0,0,.55)"/><path d="M20 15v20l16-10z" fill="#fff"/></svg>
      <div class="video-bar">
        <svg width="10" height="10" viewBox="0 0 10 10"><path d="M1 0v10l9-5z" fill="#ddd"/></svg>
        <svg width="12" height="10" viewBox="0 0 12 10"><path d="M0 3h3l4-3v10L3 7H0z" fill="#ddd"/></svg>
        <div class="video-track"><i></i></div>
        <span>01:30 / 04:55</span>
        <svg width="12" height="10" viewBox="0 0 12 10"><rect x=".5" y=".5" width="11" height="9" fill="none" stroke="#ddd"/></svg>
      </div>
    </div>
    <div class="about-copy">
      <h2 class="section-title">About <em>Company</em></h2>
      <p>Lorem Ipsum has been the industry's standard dummy text ever since the 1500s, when an unknown printer took a galley of type and scrambled it to make a type specimen book. It has survived not only five centuries, but also the leap into electronic typesetting, remaining essentially unchanged.</p>
      <p>It was popularised in the 1960s with the release of Dryletter sheets containing Lorem Ipsum passages, and more recently with desktop publishing software like Pagecraft Studio including versions of Lorem Ipsum.</p>
      <a class="btn" href="#">Read More</a>
    </div>
  </div>
</section>

<section class="testimonials">
  <div class="wrap">
    <h2 class="section-title">Testimonials</h2>
    <div class="quotes">
      <figure class="quote">
        <div class="avatar avatar-a" role="img" aria-label="Portrait of a smiling client"></div>
        <blockquote class="quote-body">
          <p>Lorem Ipsum has been the industry's standard dummy text ever since the 1500s, when an unknown printer took a galley of type and scrambled it to make</p>
          <strong>Marcus Ellery</strong>
          <span>Marketing Executive</span>
        </blockquote>
      </figure>
      <figure class="quote">
        <div class="avatar avatar-b" role="img" aria-label="Portrait of a smiling client"></div>
        <blockquote class="quote-body">
          <p>Lorem Ipsum has been the industry's standard dummy text ever since the 1500s, when an unknown printer took a galley of type and scrambled it to make</p>
          <strong>Marcus Ellery</strong>
          <span>Marketing Executive</span>
        </blockquote>
      </figure>
    </div>
  </div>
</section>

<section class="memberships">
  <div class="wrap">
    <h4>Membership<br><em>Logos</em></h4>
    <div class="member"><svg class="member-badge" viewBox="0 0 48 48"><rect width="48" height="48" fill="#1aa39a"/></svg>YQK</div>
    <div class="member"><svg class="member-badge" viewBox="0 0 48 48"><rect width="48" height="48" fill="#8b1c2b"/></svg>JZV</div>
    <div class="member"><svg class="member-badge" viewBox="0 0 48 48"><rect width="48" height="48" fill="#7b4a9b"/></svg>QXW</div>
    <div class="member"><svg class="member-badge" viewBox="0 0 48 48"><circle cx="24" cy="24" r="24" fill="#2b7fc1"/></svg>safehold-example.co.uk</div>
  </div>
</section>

<footer class="site-footer">
  <div class="wrap footer-cols">
    <div class="footer-col col-news">
      <h5>Newsletters Sign Up</h5>
      <p>Sign up for our daily email by entering<br>your information below</p>
      <div class="email-field">Email address</div>
      <span class="subscribe">SUBSCRIBE</span>
    </div>
    <div class="footer-col col-tweet">
      <h5>Latest Tweet</h5>
      <div class="tweet"><span class="tweet-dot"></span><p>Featured Workspace : Brickline Studio<br>brkl.example/7Qx2 <em>10 hours ago</em></p></div>
      <div class="tweet"><span class="tweet-dot"></span><p>Featured Workspace : Brickline Studio<br>brkl.example/7Qx2 <em>10 hours ago</em></p></div>
    </div>
    <div class="footer-col col-contact">
      <h5>Get In Touch</h5>
      <ul class="contact-list">
        <li>Address : 12 Harbour Row, Redcliffe<br>Bristol, BS1 9ZZ</li>
        <li>Phone : 0117 555 0142</li>
        <li>Email : hello@thornburylettings.example</li>
      </ul>
    </div>
    <div class="footer-col col-follow">
      <h5>Follow Us On</h5>
      <ul class="social">
        <li><span class="social-dot"></span>Flockpage</li>
        <li><span class="social-dot"></span>Chirpline</li>
        <li><span class="social-dot"></span>Snapframe</li>
      </ul>
    </div>
  </div>
</footer>
<div class="copyright">Copyright © 2016. All Rights Reserved</div>

</body>
</html>
```